Modern claims management company

We need a new company presentation brochure, composed of about 20 pages in A4 format.
Cover, page 1 who we are, page 2 company profile, page 3 territorial operation, page from 4 to 10 services offered and description of services (The title of the page are: Perizie e Liquidazione danni, riparazioni e sostituzioni, teleclaimer, accertamento danni da fenomeno elettrico, TPA, Auditing, drone pilot, Valutazione rischi), from 11 to 17 specializations (Sinistri gravi, R.C., Tecnologici, Energie rinnovabili, strutture, ambiente) page 18 e 19 integrated services (perdite occulte, ricerca guasti, indagini termografiche, crisis management), page 20 clients ( list companies and logos) page 21 contact.
The company is made up of various companies, which belong to the principal, each of which deals with specific activities.
To date we already have various logos of the main company (Tavesi and Durando) as well as the logos of the other companies. I load them on the portal.
Found then the graphic solution that we like we will have to proceed to make a presentation in similar powerpoint and the website.

Target Market(s)

Insurance Company, Insurance Broker

Other font styles liked:
• ARIAL

Colors
333333
5c5c5c
959595
0392cd

Requirements
Must have
• It must be clear, professional and modern.
Nice to have
• I indicate some competitor sites, so that you can better understand what we are doing. www.fenwoodhale.com, www.harrowpikestead.com, www.orsavantini.com, www.gruppotessandi.com, www.vandrini.eu.

```html
<!DOCTYPE html>
<html lang="it">
<head>
<meta charset="utf-8">
<title>Tavesi &amp; Durando – Brochure</title>
<link rel="stylesheet" href="https://fonts.googleapis.com/css2?family=Bree+Serif&family=Open+Sans:wght@400;600&family=PT+Serif:ital,wght@1,700&display=swap">
<style>
:root{
  --stage:#3b3b3b;
  --blue:#1d6cb4;
  --navy:#164f8c;
  --cyan:#0392cd;
  --ink:#333333;
  --grey:#5c5c5c;
  --mid:#959595;
  --paper:#ffffff;
}
*{margin:0;padding:0;box-sizing:border-box}
html,body{width:1200px;height:3082px;overflow:hidden;background:var(--stage)}
body{position:relative;font-family:"Open Sans",Arial,sans-serif;color:var(--ink)}
.spread{position:absolute;left:99px;width:1002px;height:709px}
.page{position:absolute;top:0;width:501px;height:709px;overflow:hidden;background:var(--paper)}
.page--left{left:0;background:linear-gradient(90deg,#fff 80%,#e6e6e6)}
.page--right{left:501px;background:linear-gradient(90deg,#e4e4e4,#fff 18%)}
.abs{position:absolute}
.fill{position:absolute;left:0;top:0;width:100%;height:100%}
.heading{position:absolute;font-family:"Bree Serif",Georgia,serif;color:var(--navy);font-size:20px;line-height:1}
.copy{position:absolute;font-size:10.5px;line-height:13px;color:var(--grey);text-align:justify}
.copy p+p{margin-top:13px}
.brand{font-family:"Open Sans",Arial,sans-serif;font-weight:400;color:#fff;font-size:34px;line-height:1;white-space:nowrap}
.brand-sub{font-size:13px;color:#fff;margin-top:4px;letter-spacing:.3px}
.contact{position:absolute;left:0;width:501px;top:610px;text-align:center;color:#fff;font-family:Georgia,"Times New Roman",serif;font-size:14px;line-height:19px}
.cover-claim{position:absolute;left:330px;top:120px;width:120px;text-align:center;color:#fff;font-size:38px;line-height:48px}
.profile-box{position:absolute;left:45px;top:216px;width:411px;height:331px;background:#fff;border:2px solid var(--navy)}
.feature{position:absolute;width:150px;text-align:center}
.feature-dot{width:40px;height:40px;border-radius:50%;background:var(--navy);margin:0 auto 6px}
.feature-title{font-family:"Bree Serif",Georgia,serif;font-size:8px;color:var(--navy);margin-bottom:6px}
.feature-text{font-size:8.5px;line-height:11px;color:var(--ink)}
.note-box{position:absolute;left:45px;top:565px;width:411px;height:72px;border:2px solid #fff;padding:8px 10px;color:#fff;font-size:10.5px;line-height:13px}
.quote{position:absolute;font-family:"PT Serif",Georgia,serif;font-style:italic;font-weight:700;color:#fff;font-size:12.5px;line-height:16px;text-align:right}
.quote-mark{font-family:Georgia,serif;font-weight:700;font-size:46px;line-height:1;color:var(--navy);position:absolute}
.panel-dark{position:absolute;left:45px;top:80px;width:417px;height:401px;background:#5c5c5c;padding:24px 28px}
.panel-dark .heading{position:static;color:#fff;margin-bottom:14px}
.panel-dark .copy{position:static;color:#eee}
.panel-blue{position:absolute;left:435px;top:526px;width:528px;height:105px;background:var(--navy);padding:10px 30px 0 120px;color:#fff;font-size:10.5px;line-height:13px}
</style>
</head>
<body>

<!-- Cover -->
<section class="spread" style="top:99px">
  <div class="page page--left" style="background:var(--blue)">
    <div class="abs" style="left:100px;top:520px">
      <div class="brand">Tavesi &amp; Durando</div>
      <div class="brand-sub">consulenza peritale per le assicurazioni</div>
    </div>
    <div class="contact">Ph: 000 000 0000 | Fax: 000 000 0000<br>Email: info@tavesidurando.it<br>www.tavesidurando.com</div>
  </div>
  <div class="page page--right" style="background:#fff">
    <svg class="fill" viewBox="0 0 501 709" aria-hidden="true">
      <defs>
        <linearGradient id="coverBand" x1="0" y1="0" x2="1" y2="0">
          <stop offset="0" stop-color="#e6e6e6"/><stop offset="1" stop-color="#a5a5a5"/>
        </linearGradient>
      </defs>
      <rect x="0" y="0" width="501" height="90" fill="url(#coverBand)"/>
      <polygon points="180,0 501,0 501,520" fill="var(--blue)"/>
      <line x1="150" y1="0" x2="501" y2="568" stroke="var(--cyan)" stroke-width="3"/>
      <rect x="0" y="86" width="501" height="4" fill="var(--blue)"/>
    </svg>
    <div class="cover-claim">Your Text here</div>
    <div class="abs" style="left:43px;top:610px">
      <div class="brand" style="color:var(--blue);font-size:30px">Tavesi &amp; Durando</div>
      <div class="brand-sub" style="color:var(--blue)">consulenza peritale per le assicurazioni</div>
    </div>
  </div>
</section>

<!-- Who we are / Company profile -->
<section class="spread" style="top:826px">
  <div class="page page--left">
    <h2 class="heading" style="left:39px;top:46px">who we are</h2>
    <div class="copy" style="left:39px;top:78px;width:413px">
      <p>Lorem ipsum dolor sit amet, consectetuer adipiscing elit, sed diam nonummy nibh euismod tincidunt ut laoreet dolore magna aliquam erat volutpat. Ut wisi enim ad minim veniam, quis nostrud exerci tation ullamcorper suscipit lobortis nisl ut aliquip ex ea commodo consequat. Duis autem vel eum iriure dolor in hendrerit in vulputate velit esse molestie consequat, vel illum dolore eu feugiat nulla facilisis at vero eros et accumsan et iusto odio dignissim qui blandit praesent luptatum zzril delenit augue duis dolore te feugait nulla facilisi.</p>
      <p>Lorem ipsum dolor sit amet, cons ectetuer adipiscing elit, sed diam nonummy nibh euismod tincidunt ut laoreet dolore magna aliquam erat volutpat. Ut wisi enim ad minim veniam, quis nostrud exerci tation ullamcorper suscipit lobortis nisl ut aliquip ex ea commodo consequat.</p>
      <p>Lorem ipsum dolor sit amet, consectetuer adipiscing elit, sed diam nonummy nibh euismod tincidunt ut laoreet dolore magna aliquam erat volutpat. Ut wisi enim ad minim veniam, quis nostrud exerci tation ullamcorper suscipit lobortis nisl ut aliquip ex ea commodo consequat.</p>
    </div>
    <svg class="fill" viewBox="0 0 501 709" role="img" aria-label="Photo: two business people in a meeting at an office desk">
      <defs><linearGradient id="meetPhoto" x1="0" y1="0" x2="1" y2="0"><stop offset="0" stop-color="#c9b79f"/><stop offset="1" stop-color="#6d6660"/></linearGradient></defs>
      <polygon points="0,330 501,470 501,490 0,345" fill="#d8d8d8"/>
      <polygon points="0,345 501,490 501,600 0,709" fill="url(#meetPhoto)"/>
      <polygon points="0,709 501,590 501,709" fill="var(--navy)"/>
      <line x1="0" y1="700" x2="501" y2="582" stroke="#fff" stroke-width="5"/>
    </svg>
  </div>
  <div class="page page--right">
    <svg class="fill" viewBox="0 0 501 709" aria-hidden="true">
      <polygon points="0,600 501,330 501,709 0,709" fill="var(--navy)"/>
    </svg>
    <h2 class="heading" style="left:33px;top:46px">company profile</h2>
    <div class="copy" style="left:33px;top:78px;width:436px">
      <p>Lorem ipsum dolor sit amet, consectetuer adipiscing elit, sed diam nonummy nibh euismod tincidunt ut laoreet dolore magna aliquam erat volutpat. Ut wisi enim ad minim veniam, quis nostrud exerci tation ullamcorper suscipit lobortis nisl ut aliquip ex ea commodo consequat. Duis autem vel eum iriure dolor in hendrerit in vulputate velit esse molestie consequat, vel illum dolore eu feugiat nulla facilisis at vero eros et accumsan et iusto odio dignissim qui blandit praesent luptatum zzril delenit augue duis dolore te feugait nulla facilisi.</p>
    </div>
    <div class="profile-box">
      <div class="feature" style="left:26px;top:38px"><div class="feature-dot"></div><div class="feature-title">Text Here</div><div class="feature-text">Lorem ipsum dolor sit amet, consectetuer adipiscing elit, sed diam nonummy nibh euismod tincidunt ut laoreet</div></div>
      <div class="feature" style="left:231px;top:38px"><div class="feature-dot"></div><div class="feature-title">Text Here</div><div class="feature-text">Lorem ipsum dolor sit amet, consectetuer adipiscing elit, sed diam nonummy nibh euismod tincidunt ut laoreet</div></div>
      <div class="feature" style="left:26px;top:178px"><div class="feature-dot"></div><div class="feature-title">Text Here</div><div class="feature-text">Lorem ipsum dolor sit amet, consectetuer adipiscing elit, sed diam nonummy nibh euismod tincidunt ut laoreet</div></div>
      <div class="feature" style="left:231px;top:178px"><div class="feature-dot"></div><div class="feature-title">Text Here</div><div class="feature-text">Lorem ipsum dolor sit amet, consectetuer adipiscing elit, sed diam nonummy nibh euismod tincidunt ut laoreet</div></div>
    </div>
    <div class="note-box">Lorem ipsum dolor sit amet, consectetuer adipiscing elit, sed diam nonummy nibh euismod tincidunt ut laoreet dolore magna aliquam erat volutpat. Ut wisi enim ad minim veniam, quis nostrud exerci tation ullamcorper suscipit lobortis nisl ut aliquip ex ea commodo consequat.</div>
  </div>
</section>

<!-- Territorial operation / Our services -->
<section class="spread" style="top:1552px">
  <div class="page page--left">
    <svg class="fill" viewBox="0 0 501 709" aria-hidden="true">
      <polygon points="210,709 501,585 501,709" fill="var(--navy)"/>
    </svg>
    <h2 class="heading" style="left:39px;top:51px">Territorial Operation</h2>
    <div class="copy" style="left:39px;top:75px;width:423px">
      <p>Lorem ipsum dolor sit amet, consectetuer adipiscing elit, sed diam nonummy nibh euismod tincidunt ut laoreet dolore magna aliquam erat volutpat. Ut wisi enim ad minim veniam, quis nostrud exerci tation ullamcorper suscipit lobortis nisl ut aliquip ex ea commodo consequat. Duis autem vel eum iriure dolor in hendrerit in vulputate velit esse molestie consequat, vel illum dolore eu feugiat nulla facilisis at vero eros et accumsan et iusto odio dignissim qui blandit praesent luptatum zzril delenit augue duis dolore te feugait nulla facilisi.</p>
      <p>Lorem ipsum dolor sit amet, cons ectetuer adipiscing elit, sed diam nonummy nibh euismod tincidunt ut laoreet dolore magna aliquam erat volutpat.</p>
    </div>
    <div class="abs" role="img" aria-label="Photo: business handshake in front of colleagues" style="left:39px;top:238px;width:423px;height:228px;background:linear-gradient(135deg,#c7ccd4,#6f7680 60%,#3a3f48)"></div>
    <h2 class="heading" style="left:39px;top:493px">Territorial Operation</h2>
    <div class="copy" style="left:39px;top:515px;width:423px">
      <p>Lorem ipsum dolor sit amet, consectetuer adipiscing elit, sed diam nonummy nibh euismod tincidunt ut laoreet dolore magna aliquam erat volutpat. Ut wisi enim ad minim veniam, quis nostrud exerci tation ullamcorper suscipit lobortis nisl ut aliquip ex ea commodo consequat. Duis autem vel eum iriure dolor in hendrerit in vulputate velit esse molestie consequat, vel illum dolore eu feugiat nulla facilisis at vero eros et accumsan et iusto odio dignissim qui blandit praesent luptatum zzril delenit augue duis dolore te feugait nulla facilisi.</p>
      <p>Lorem ipsum dolor sit amet, cons ectetuer adipiscing elit, sed diam nonummy nibh euismod tincidunt ut laoreet dolore magna aliquam erat volutpat.</p>
    </div>
  </div>
  <div class="page page--right">
    <svg class="fill" viewBox="0 0 501 709" role="img" aria-label="Photo: smiling businessman in a suit leaning on a board">
      <defs><linearGradient id="manPhoto" x1="0" y1="0" x2="0" y2="1"><stop offset="0" stop-color="#d9d9d9"/><stop offset=".35" stop-color="#3a3d44"/><stop offset="1" stop-color="#23262c"/></linearGradient></defs>
      <polygon points="12,41 222,41 222,505 12,583" fill="url(#manPhoto)"/>
      <polygon points="0,585 501,400 501,709 0,709" fill="var(--navy)"/>
      <line x1="150" y1="548" x2="501" y2="418" stroke="var(--cyan)" stroke-width="5"/>
    </svg>
    <h2 class="heading" style="left:232px;top:104px;font-size:18px">Our services</h2>
    <div class="copy" style="left:232px;top:128px;width:240px">
      <p>Lorem ipsum dolor sit amet, consectetuer adipiscing elit, sed diam nonummy nibh euismod tincidunt ut laoreet dolore magna aliquam erat volutpat. Ut wisi enim ad minim veniam, quis nostrud exerci tation ullamcorper suscipit lobortis nisl ut aliquip ex ea commodo consequat.</p>
      <p>Duis autem vel eum iriure dolor in hendrerit in vulputate velit esse molestie consequat, vel illum dolore eu feugiat nulla facilisis at vero eros et accumsan et iusto odio dignissim qui blandit praesent luptatum zzril delenit augue duis dolore te feugait nulla facilisi.</p>
      <p>Lorem ipsum dolor sit amet, cons ectetuer adipiscing elit, sed diam nonummy nibh euismod tincidunt ut laoreet dolore magna aliquam erat volutpat. Ut wisi enim ad minim veniam, quis nostrud exerci tation ullamcorper suscipit lobortis nisl ut aliquip ex ea commodo consequat.</p>
      <p>Lorem ipsum dolor sit amet, consectetuer adipiscing elit.</p>
    </div>
    <span class="quote-mark" style="left:412px;top:428px">”</span>
    <span class="quote-mark" style="left:226px;top:566px;color:#fff">“</span>
    <p class="quote" style="left:250px;top:580px;width:222px">Lorem ipsum dolor sit amet, consectetuer adipiscing elit, sed diam nonummy nibh euismod tincidunt ut laoreet dolore magna</p>
    <span class="quote-mark" style="left:452px;top:656px;color:#fff">”</span>
  </div>
</section>

<!-- Our services -->
<section class="spread" style="top:2273px">
  <div class="page page--left">
    <svg class="fill" viewBox="0 0 501 709" aria-hidden="true">
      <polygon points="250,0 501,0 501,50" fill="var(--navy)"/>
    </svg>
    <h2 class="heading" style="left:32px;top:57px;font-size:18px">Our services</h2>
    <div class="copy" style="left:32px;top:80px;width:440px">
      <p>Lorem ipsum dolor sit amet, consectetuer adipiscing elit, sed diam nonummy nibh euismod tincidunt ut laoreet dolore magna aliquam erat volutpat. Ut wisi enim ad minim veniam, quis nostrud exerci tation ullamcorper suscipit lobortis nisl ut aliquip ex ea commodo consequat.</p>
      <p>Duis autem vel eum iriure dolor in hendrerit in vulputate velit esse molestie consequat, vel illum dolore eu feugiat nulla facilisis at vero eros et accumsan et iusto odio dignissim qui blandit praesent luptatum zzril delenit augue duis dolore te feugait nulla facilisi.</p>
      <p>Lorem ipsum dolor sit amet, cons ectetuer adipiscing elit, sed diam nonummy nibh euismod tincidunt ut laoreet dolore magna aliquam erat volutpat. Ut wisi enim ad minim veniam, quis nostrud exerci tation ullamcorper suscipit lobortis nisl ut aliquip ex ea commodo consequat.</p>
    </div>
    <div class="abs" role="img" aria-label="Photo: team of three business people standing with arms crossed" style="left:0;top:275px;width:501px;height:339px;background:linear-gradient(90deg,#2e2a29 0%,#5d564f 40%,#c9c4bc 75%,#e6e3de)"></div>
    <div class="abs" style="left:0;top:614px;width:436px;height:10px;background:var(--navy)"></div>
    <div class="copy" style="left:32px;top:632px;width:440px">
      <p>Lorem ipsum dolor sit amet, consectetuer adipiscing elit, sed diam nonummy nibh euismod tincidunt ut laoreet dolore magna aliquam erat volutpat. Ut wisi enim ad minim veniam.</p>
    </div>
  </div>
  <div class="page page--right">
    <svg class="fill" viewBox="0 0 501 709" aria-hidden="true">
      <polygon points="0,0 501,0 501,360 0,20" fill="var(--navy)"/>
      <line x1="0" y1="34" x2="501" y2="375" stroke="var(--cyan)" stroke-width="5"/>
      <polygon points="260,709 501,540 501,709" fill="var(--navy)"/>
    </svg>
    <div class="panel-dark">
      <h2 class="heading" style="font-size:18px">Our services</h2>
      <div class="copy">
        <p>Lorem ipsum dolor sit amet, consectetuer adipiscing elit, sed diam nonummy nibh euismod tincidunt ut laoreet dolore magna aliquam erat volutpat. Ut wisi enim ad minim veniam, quis nostrud exerci tation ullamcorper suscipit lobortis nisl ut aliquip ex ea commodo consequat.</p>
        <p>Duis autem vel eum iriure dolor in hendrerit in vulputate velit esse molestie consequat, vel illum dolore eu feugiat nulla facilisis at vero eros et accumsan et iusto odio dignissim qui blandit praesent luptatum zzril delenit augue duis dolore te feugait nulla facilisi.</p>
        <p>Lorem ipsum dolor sit amet, cons ectetuer adipiscing elit, sed diam nonummy nibh euismod tincidunt ut laoreet dolore magna aliquam erat volutpat. Ut wisi enim ad minim veniam, quis nostrud exerci tation ullamcorper suscipit lobortis nisl ut aliquip ex ea commodo consequat.</p>
      </div>
      <div style="position:relative;margin-top:18px;height:80px">
        <span class="quote-mark" style="left:0;top:-8px;color:#fff">“</span>
        <p class="quote" style="position:absolute;left:30px;top:4px;width:300px;text-align:center">Lorem ipsum dolor sit amet, consectetuer adipiscing elit, sed diam nonummy nibh euismod tincidunt ut laoreet dolore magna</p>
        <span class="quote-mark" style="left:330px;top:44px;color:#fff">”</span>
      </div>
    </div>
  </div>
  <div class="panel-blue">Lorem ipsum dolor sit amet, consectetuer adipiscing elit, sed diam nonummy nibh euismod tincidunt ut laoreet dolore magna aliquam erat volutpat. Ut wisi enim ad minim veniam, quis nostrud exerci tation ullamcorper suscipit lobortis nisl ut aliquip ex ea commodo consequat. Lorem ipsum dolor sit amet, consectetuer adipiscing elit, sed diam nonummy nibh euismod tincidunt ut laoreet dolore magna aliquam erat volutpat. Ut wisi enim ad minim veniam.</div>
</section>

</body>
</html>
```